Stationary and design update for my brand

I need new letterhead, a new business card, business envelope design, new keynote and powerpoint branded slides (16x9). I have logo samples in various styles and brand standards for fonts and colors.

Font styles to use
Sans Serif

```html
<!DOCTYPE html>
<html lang="en">
<head>
<meta charset="utf-8">
<title>Alder Crest – Business Card</title>
<link href="https://fonts.googleapis.com/css2?family=Roboto:wght@400;700&display=swap" rel="stylesheet">
<style>
  :root {
    --backdrop: #2b2b2d;
    --card: #ffffff;
    --accent: #f2a531;
    --ink: #4a4a4a;
    --bar: #231f20;
    --sky-top: #5b5f9c;
    --sky-mid: #e98e8a;
    --sky-warm: #f7b27a;
    --rock: #4e546e;
    --white: #ffffff;
  }
  * { margin: 0; padding: 0; box-sizing: border-box; }
  html, body { width: 1200px; height: 929px; overflow: hidden; }
  body {
    background: var(--backdrop);
    font-family: "Roboto", Arial, sans-serif;
    position: relative;
  }
  .card {
    position: absolute;
    width: 560px;
    height: 320px;
    box-shadow: 0 10px 30px rgba(0,0,0,.45);
    overflow: hidden;
  }
  /* Front */
  .card--front { left: 70px; top: 70px; }
  .front-photo {
    position: absolute; inset: 0;
    background:
      linear-gradient(180deg, rgba(0,0,0,0) 55%, var(--rock) 100%),
      linear-gradient(160deg, var(--sky-top) 0%, var(--sky-mid) 45%, var(--sky-warm) 75%, #c9c3cf 100%);
  }
  .front-brand {
    position: absolute; left: 0; right: 0; top: 110px;
    text-align: center; color: var(--white);
  }
  .front-brand__name {
    font-weight: 400; font-size: 58px; letter-spacing: 3px; line-height: 1;
  }
  .front-brand__tagline {
    margin-top: 34px; font-size: 15px; letter-spacing: .3px;
  }
  /* Back */
  .card--back { left: 570px; top: 520px; width: 580px; height: 331px; background: var(--card); }
  .back-brand {
    position: absolute; right: 36px; top: 44px;
    color: var(--accent); font-weight: 400; font-size: 36px; letter-spacing: 1px;
  }
  .back-bar {
    position: absolute; left: 0; top: 196px; width: 40px; height: 22px; background: var(--bar);
  }
  .contact {
    position: absolute; left: 58px; top: 140px; color: var(--ink);
  }
  .contact__name { color: var(--accent); font-weight: 700; font-size: 17px; }
  .contact__role { font-size: 15px; margin-top: 2px; }
  .contact__list { list-style: none; margin-top: 6px; }
  .contact__item { display: flex; align-items: center; gap: 8px; font-size: 15px; line-height: 21px; }
  .contact__item svg { width: 14px; height: 14px; flex: none; }
  .contact__address { margin-top: 4px; font-size: 15px; line-height: 20px; }
</style>
</head>
<body>
  <section class="card card--front">
    <div class="front-photo" role="img" aria-label="Photograph of a snowy mountain peak under a violet and peach sunrise sky"></div>
    <div class="front-brand">
      <div class="front-brand__name">Alder Crest</div>
      <p class="front-brand__tagline">Empowering Individual and Organizational Transformation!</p>
    </div>
  </section>

  <section class="card card--back">
    <div class="back-brand">Alder Crest</div>
    <div class="back-bar"></div>
    <div class="contact">
      <p class="contact__name">Daniel Marsh-Everly, DMIN, PCC</p>
      <p class="contact__role">Owner / Trainer / Coach / Consultant</p>
      <ul class="contact__list">
        <li class="contact__item">
          <svg viewBox="0 0 16 16" aria-hidden="true"><path fill="#f2a531" d="M3 1l3 3-2 2c1 2 3 4 5 5l2-2 3 3-2 3C7 15 1 9 1 3z"/></svg>
          (555) 014-2890
        </li>
        <li class="contact__item">
          <svg viewBox="0 0 16 16" aria-hidden="true"><rect x="1" y="3" width="14" height="10" fill="#f2a531"/><path d="M1 3l7 6 7-6" fill="none" stroke="#fff" stroke-width="1.4"/></svg>
          daniel@aldercrestcbc.com
        </li>
        <li class="contact__item">
          <svg viewBox="0 0 16 16" aria-hidden="true"><g fill="none" stroke="#f2a531" stroke-width="1.5"><circle cx="8" cy="8" r="6.5"/><ellipse cx="8" cy="8" rx="3" ry="6.5"/><path d="M1.5 8h13"/></g></svg>
          www.aldercrestcbc.com
        </li>
      </ul>
      <p class="contact__address">Alder Crest Coaching and Behavioral Consulting LLC<br>4820 Linden Ridge Dr. Plano, TX 75024</p>
    </div>
  </section>
</body>
</html>
```